Vision Board Class Design needed

Hello, I need a business card design for a new Company based in Mount Waverley, Victoria, Australia. The Company provides a training Class with approx. 5 guests. They learn how to choose and create positive things in their life. It is based on the principal of the Law of Attraction. Each guest receives a large coloured cardboard and magazines, affirmations to choose ideas to help create their new exciting life - all pasted onto a "Vision Board" which will be seen by them every day and help to clarify the vision and attract abundance, happiness & positivity into their lives. I would like to see designs with bright, happy colours - perhaps rainbows - anything that represents a new life and appears refreshing.
Many thanks.

Industry/Entity Type

Training

Contact Information for Business Card

Dream Harbour
Lorna
Mobile 0473 259-386

Logo Text

Dream Harbour

Logo styles of interest
Abstract Logo
Requirements
Must have
• Happy, Bright colours!

```html
<!DOCTYPE html>
<html lang="en">
<head>
<meta charset="utf-8">
<title>Dream Harbour – Business Card</title>
<link rel="stylesheet" href="https://fonts.googleapis.com/css2?family=Lobster&family=Lato:wght@300&display=swap">
<style>
  :root {
    --backdrop: #d9dadc;
    --card-plum: #4e1f4c;
    --accent-yellow: #f5d61c;
    --text-soft: #e6d8e6;
    --mosaic-pink: #e8237f;
    --mosaic-orange: #f37a21;
    --mosaic-yellow: #f3e51d;
    --mosaic-green: #8cc63f;
    --mosaic-cyan: #1fb5d6;
    --mosaic-violet: #a0449b;
  }
  html, body {
    margin: 0;
    width: 1200px;
    height: 864px;
    overflow: hidden;
    background: var(--backdrop);
  }
  .card {
    position: absolute;
    left: 110px;
    top: 152px;
    width: 980px;
    height: 560px;
    background: var(--card-plum);
    box-shadow: 0 18px 40px rgba(0,0,0,0.25);
    overflow: hidden;
  }
  .card__mosaic {
    position: absolute;
    inset: 0;
    width: 100%;
    height: 100%;
  }
  .card__identity {
    position: absolute;
    right: 70px;
    top: 175px;
    text-align: left;
  }
  .card__brand {
    margin: 0;
    font-family: "Lobster", cursive;
    font-weight: 400;
    font-size: 64px;
    color: var(--accent-yellow);
    line-height: 1;
  }
  .card__contact {
    margin: 16px 0 0;
    font-family: "Lato", sans-serif;
    font-weight: 300;
    font-size: 30px;
    color: var(--text-soft);
    letter-spacing: 1px;
  }
  .card__person {
    font-family: "Lobster", cursive;
    color: var(--accent-yellow);
    font-size: 32px;
    letter-spacing: 0;
  }
</style>
</head>
<body>
  <section class="card">
    <svg class="card__mosaic" viewBox="0 0 980 560" role="img" aria-label="Rainbow triangle mosaic bands in pink, orange, yellow, green, cyan and violet">
      <defs>
        <linearGradient id="rainbow" x1="0" y1="0" x2="1" y2="0.4">
          <stop offset="0" stop-color="var(--mosaic-cyan)"/>
          <stop offset="0.2" stop-color="var(--mosaic-pink)"/>
          <stop offset="0.4" stop-color="var(--mosaic-orange)"/>
          <stop offset="0.6" stop-color="var(--mosaic-yellow)"/>
          <stop offset="0.8" stop-color="var(--mosaic-green)"/>
          <stop offset="1" stop-color="var(--mosaic-violet)"/>
        </linearGradient>
      </defs>
      <g class="mosaic-band" fill="url(#rainbow)">
        <polygon points="0,60 980,60 980,110 0,110"/>
        <polygon points="0,110 620,110 560,170 0,170"/>
        <polygon points="0,170 520,170 470,230 0,230"/>
        <polygon points="0,230 300,230 250,290 0,290"/>
        <polygon points="330,230 430,230 380,290 280,290"/>
        <polygon points="0,290 220,290 160,350 0,350"/>
        <polygon points="0,350 130,350 80,410 0,410"/>
        <polygon points="170,350 260,350 210,410 120,410"/>
        <polygon points="0,410 60,410 30,470 0,470"/>
      </g>
    </svg>
    <div class="card__identity">
      <h1 class="card__brand">Dream Harbour</h1>
      <p class="card__contact"><span class="card__person">Lorna</span> • 0473 259-386</p>
    </div>
  </section>
</body>
</html>
```